Full Service Day Spa Needs Wordpress Template Designed

Willowmere Spa is a full service day spa, where we make our own line of bath and body products. The current website houses an online store with an ShopNexa base (as a WordPress plugin) and simple web pages with information and price lists for services.
For the upgraded website, we are doing a significant makeover and want to include the ability to have full screen video on our main page, windowed or full screen video on feature pages (for example, pages for "Meet our staff" or "Product Demos")
The site should retain standard WordPress compatibility for plugins, such as galleries etc.
The ability to include iframes would be considered a plus so that we can embed external scheduling applications that we subscribe to.
The color scheme for our spa features chocolate brown, taupe, cream, and turquoise for color accents. We would like our website to reflect these colors as our customers find them relaxing.
Our spa has a number of paintings on our walls, which could be used for inspiration for the website design. We like modern abstract art, with curves and swirls. I have included examples of this artwork so that potential designers can see what we like.
The new site must include our logo (provided) and our tag line: "Come Relax With Us" displayed in the upper left in the header.
We would prefer to have the option to put the menu either on the left side, or across the top to the right of the logo.
Words to describe the look we are seeking would be elegant, upscale, relaxing.

Target Market(s)

Our market is primarily local women (in and around our city) who are professionals aged 30 - 65.

Industry/Entity Type

Store

Colors
f78f20
00a990
f37022

Requirements
Must have
• The template should accommodate full screen and partial screen HTML5 video. Must have a menu, could be top or could be side. Should be in shades of browns and neutral colors, with teal accents, or similar highlights to the attached pictures of our artwork we have in the spa. We are looking for a consistent look that our customers can identify is us. Must have our logo in the upper left side of the header.
Nice to have
• Iframes built in would be nice, although we know we can get plugins for that. Likewise we know we can get plugins for the HTML 5 video, we would like the template built with accommodating that in mind. We have seen sites that have full screen video on the main page. We think this looks good.
Should not have
• We are looking for something elegant and upscale, so we are not looking for something "Cartoonish".

```html
<!DOCTYPE html>
<html lang="en">
<head>
<meta charset="utf-8">
<title>Willowmere Spa</title>
<link href="https://fonts.googleapis.com/css2?family=Comfortaa:wght@400;700&family=Arimo:wght@400;700&display=swap" rel="stylesheet">
<style>
:root{
  --cocoa:#3b302b;
  --cocoa-soft:#4a3c35;
  --taupe:#b38c6c;
  --panel:rgba(248,246,244,.96);
  --panel-line:#e4ded9;
  --text:#5a524d;
  --muted:#8d8580;
  --dot:#c9c5c2;
  --dot-active:#b08866;
  --warm-1:#f0a76a;
  --warm-2:#c86a2c;
  --warm-3:#7a3d1c;
}
*{box-sizing:border-box;margin:0;padding:0}
html,body{width:897px;height:1200px;overflow:hidden}
body{font-family:"Arimo",Arial,sans-serif;color:var(--text)}
.canvas{position:relative;width:897px;height:1200px;overflow:hidden}
.backdrop{position:absolute;inset:0;background:radial-gradient(ellipse at 70% 40%,var(--warm-1) 0%,var(--warm-2) 45%,var(--warm-3) 100%)}
.panel{position:absolute;background:var(--panel);box-shadow:0 2px 10px rgba(60,30,10,.25)}

.sidebar{left:64px;top:16px;width:236px;height:682px}
.brand{position:absolute;left:0;top:40px;width:100%;text-align:center}
.brand-mark{width:44px;height:44px;border-radius:50%;background:var(--taupe);margin:0 auto 10px}
.brand-name{font-family:"Comfortaa",sans-serif;font-weight:700;font-size:25px;color:var(--cocoa)}
.brand-tagline{font-family:"Comfortaa",sans-serif;font-weight:700;font-size:9px;color:var(--cocoa);margin-top:4px}
.brand-rule{position:absolute;left:20px;right:20px;top:146px;height:1px;background:linear-gradient(90deg,transparent,#cfc8c2,transparent)}
.main-nav{position:absolute;left:10px;right:10px;top:175px;list-style:none}
.main-nav li{height:38.6px;line-height:38.6px;padding-left:77px;border-bottom:1px solid var(--panel-line);font-family:"Comfortaa",sans-serif;font-size:15px;color:var(--taupe)}
.main-nav li.current{color:var(--cocoa)}
.main-nav li:last-child{border-bottom:none}
.welcome-title{position:absolute;left:0;right:0;top:478px;text-align:center;font-family:"Comfortaa",sans-serif;font-weight:400;font-size:24px;line-height:30px;color:var(--cocoa)}
.welcome-rule{position:absolute;left:40px;right:40px;top:514px;height:1px;background:linear-gradient(90deg,transparent,#cfc8c2,transparent)}
.welcome-text{position:absolute;left:6px;right:6px;top:525px;text-align:center;white-space:nowrap;font-size:10.3px;line-height:14px;color:var(--muted)}
.btn{display:inline-block;background:var(--cocoa);color:#fff;font-size:10px;text-align:center}
.read-more{position:absolute;left:67px;top:607px;width:101px;height:44px;line-height:44px}

.slider{left:310px;top:16px;width:523px;height:320px}
.slide-image{position:absolute;left:0;top:0;width:100%;height:288px;background:linear-gradient(120deg,#2a1a12 0%,#6b4530 40%,#d9b49a 70%,#e9a9bd 100%)}
.slider-bar{position:absolute;left:0;top:288px;width:100%;height:32px;background:#fff}
.arrow{position:absolute;top:0;width:32px;height:32px;background:var(--cocoa-soft)}
.arrow.prev{left:0}.arrow.next{right:0}
.arrow svg{position:absolute;left:11px;top:9px}
.dots{position:absolute;left:233px;top:9px;display:flex;gap:6px}
.dots span{width:14px;height:14px;border-radius:50%;background:var(--dot)}
.dots span.active{background:var(--dot-active)}

.section-title{font-family:"Comfortaa",sans-serif;font-weight:400;font-size:29px;color:var(--cocoa);text-align:center}
.section-rule{height:1px;margin:12px auto 0;width:60%;background:linear-gradient(90deg,transparent,#bdb5ae,transparent)}

.staff{left:310px;top:362px;width:523px;height:336px}
.staff .section-title{margin-top:20px}
.staff-grid{position:absolute;left:12px;top:81px;width:498px;height:231px;display:grid;grid-template-columns:repeat(3,1fr);grid-template-rows:repeat(2,1fr);gap:2px}
.staff-photo{background:linear-gradient(160deg,#5b4a43,#c59c88 55%,#e2c3b2)}
.staff-photo.dim{position:relative;background:linear-gradient(160deg,#2f2a28,#6e5a50 60%,#7f6a60)}
.staff-photo.dim svg{position:absolute;left:68px;top:38px}

.products{left:64px;top:714px;width:769px;height:358px}
.products .section-title{margin-top:20px}
.product-card{position:absolute;top:83px;width:177px;height:251px;background:#fff;border:1px solid #e2dcd7;box-shadow:0 1px 3px rgba(0,0,0,.08)}
.product-photo{position:absolute;left:4px;top:4px;right:4px;height:140px}
.product-name{position:absolute;left:12px;top:158px;font-size:9px;color:#333}
.product-rule{position:absolute;left:12px;right:12px;top:180px;border-top:1px dashed #b5aea8}
.product-price{position:absolute;left:12px;top:207px;font-size:14px;color:#333}
.add-to-cart{position:absolute;right:12px;top:201px;width:75px;height:30px;line-height:30px;font-size:9px}

.site-footer{left:64px;top:1087px;width:769px;height:94px}
.social{position:absolute;left:318px;top:18px;display:flex;gap:9px}
.social span{width:28px;height:28px;border-radius:50%;background:#c4c0bd}
.copyright{position:absolute;left:179px;top:59px;font-size:10px;color:var(--muted)}
</style>
</head>
<body>
<div class="canvas">
  <div class="backdrop" role="img" aria-label="Full-page warm-toned spa photograph background"></div>

  <aside class="panel sidebar">
    <div class="brand">
      <div class="brand-mark"></div>
      <div class="brand-name">Willowmere Spa</div>
      <div class="brand-tagline">Come Relax With Us</div>
    </div>
    <div class="brand-rule"></div>
    <ul class="main-nav">
      <li class="current">Main</li>
      <li>About us</li>
      <li>Massage</li>
      <li>Staff</li>
      <li>Salon</li>
      <li>Services</li>
      <li>Contacts</li>
    </ul>
    <h2 class="welcome-title">Welcome!</h2>
    <div class="welcome-rule"></div>
    <p class="welcome-text">Lorem ipsum dolor sit amet, consectetuer<br>adipiscing elit, sed diam nonummy nibh<br>euismod tincidunt ut laoreet dolore<br>magna aliquam erat volutpat.</p>
    <span class="btn read-more">Read More</span>
  </aside>

  <section class="panel slider">
    <div class="slide-image" role="img" aria-label="Woman relaxing at a spa with candles and orchids"></div>
    <div class="slider-bar">
      <span class="arrow prev"><svg width="10" height="14" viewBox="0 0 10 14"><path d="M8 1 2 7l6 6" fill="none" stroke="#fff" stroke-width="2"/></svg></span>
      <div class="dots"><span></span><span class="active"></span><span></span></div>
      <span class="arrow next"><svg width="10" height="14" viewBox="0 0 10 14"><path d="M2 1l6 6-6 6" fill="none" stroke="#fff" stroke-width="2"/></svg></span>
    </div>
  </section>

  <section class="panel staff">
    <h2 class="section-title">Meet our staff</h2>
    <div class="section-rule"></div>
    <div class="staff-grid">
      <div class="staff-photo dim" role="img" aria-label="Staff member portrait">
        <svg width="30" height="30" viewBox="0 0 30 30"><circle cx="13" cy="13" r="9" fill="none" stroke="#fff" stroke-width="2"/><path d="M20 20l7 7M13 9v8M9 13h8" stroke="#fff" stroke-width="2"/></svg>
      </div>
      <div class="staff-photo" role="img" aria-label="Staff member portrait"></div>
      <div class="staff-photo" role="img" aria-label="Staff member portrait"></div>
      <div class="staff-photo" role="img" aria-label="Staff member portrait"></div>
      <div class="staff-photo" role="img" aria-label="Staff member portrait"></div>
      <div class="staff-photo" role="img" aria-label="Staff member portrait"></div>
    </div>
  </section>

  <section class="panel products">
    <h2 class="section-title">Latest Product</h2>
    <div class="section-rule"></div>
    <div class="product-card" style="left:13px">
      <div class="product-photo" role="img" aria-label="Manicure with nail file" style="background:linear-gradient(135deg,#f2d3c6,#e8b7a5)"></div>
      <div class="product-name">LOREM IPSUM DOLOR SIT AMET,...</div><div class="product-rule"></div>
      <div class="product-price">$121.00</div><span class="btn add-to-cart">Add to cart</span>
    </div>
    <div class="product-card" style="left:202px">
      <div class="product-photo" role="img" aria-label="Cosmetic bottles and brushes" style="background:linear-gradient(135deg,#d8d2cc,#8a7f79)"></div>
      <div class="product-name">LOREM IPSUM DOLOR SIT AMET,...</div><div class="product-rule"></div>
      <div class="product-price">$121.00</div><span class="btn add-to-cart">Add to cart</span>
    </div>
    <div class="product-card" style="left:391px">
      <div class="product-photo" role="img" aria-label="Facial treatment" style="background:linear-gradient(135deg,#a07a62,#e8cdbb)"></div>
      <div class="product-name">LOREM IPSUM DOLOR SIT AMET,...</div><div class="product-rule"></div>
      <div class="product-price">$121.00</div><span class="btn add-to-cart">Add to cart</span>
    </div>
    <div class="product-card" style="left:579px">
      <div class="product-photo" role="img" aria-label="Bath and body product bottles" style="background:linear-gradient(135deg,#1e1e1e,#c98a2a 60%,#3a3a3a)"></div>
      <div class="product-name">LOREM IPSUM DOLOR SIT AMET,...</div><div class="product-rule"></div>
      <div class="product-price">$121.00</div><span class="btn add-to-cart">Add to cart</span>
    </div>
  </section>

  <footer class="panel site-footer">
    <div class="social"><span></span><span></span><span></span><span></span></div>
    <div class="copyright">Willowmere Spa © 2014 &nbsp;/&nbsp; All Reserved</div>
  </footer>
</div>
</body>
</html>
```